develop our online residential property development appraisal service

This project requires a detailed WordPress design to represent a new digital residential property development consultancy business. At its heart it will have a number of different products that essentially advise customers of the potential value and feasibility of developing their residential site into multiple townhouses, units, apartments, etc... This will be accompanied by explaining the considerations of residential property development.

We aim to navigate and break down this complex area and provide our customers with the tools, knowledge, control and power to 'unlock the value' in their property.

REFERENCE DOCUMENTS:
1. Detailed solution requirements please refer to the attached 'wordpressdesignrequirements'
2. Logo files, style guide and colour pallet please refer to the attached 'KRMV.zip'
3. Site Map refer to attached 'wordpressdesignsitemap'

Reason: Additional information provided so extending period for designs to take into account.

Target Market(s)

The site will appeal to professional service providers; accountants, financial planners, lawyers, etc…

Industry/Entity Type

Residential

Font styles to use
Sans Serif
Other font styles liked:
• Similar to the logo font, slim line and simple

Requirements
Must have
• The logo, style and colour palette provided in the attached 'KRMV.zip' files
• Satisfy the intent of the 'wordpressdesignrequirements'
• Present as an online-centric business
• Clean, crisp and modern design
• Predominant use of white as a background contrasted with the colours provided in the colour palette
Nice to have
• Use of the following WordPress business themes is encouraged but not mandatory:
• 1. Tovu
• 2. Pilmu
• 3. Vomi
Should not have
• Overt references to Australia

```html
<!DOCTYPE html>
<html lang="en">
<head>
<meta charset="utf-8">
<title>KRMV – Residential Development Appraisals</title>
<link href="https://fonts.googleapis.com/css2?family=Open+Sans:wght@300;400;600&family=Fjalla+One&family=Encode+Sans+Condensed:wght@300;400&display=swap" rel="stylesheet">
<style>
  :root{
    --teal:#2fae9c;
    --teal-dark:#1f9c8a;
    --green:#4cbb87;
    --footer-top:#52b98a;
    --footer-bottom:#34afac;
    --ink:#2b2b2b;
    --grey:#555;
    --light-grey:#777;
    --red:#e8363b;
    --dark:#2b3838;
    --white:#fff;
  }
  *{box-sizing:border-box;margin:0;padding:0}
  html,body{width:821px;height:1200px;overflow:hidden;background:var(--white)}
  body{position:relative;font-family:"Open Sans",Arial,sans-serif;color:var(--ink)}
  .abs{position:absolute}

  /* header */
  .site-header{left:0;top:0;width:821px;height:57px;background:var(--white)}
  .brand{left:73px;top:14px;display:flex;align-items:center;gap:8px}
  .brand-mark{width:12px;height:12px;background:var(--ink)}
  .brand-name{font-family:"Open Sans",sans-serif;font-weight:600;font-size:26px;letter-spacing:1px;color:var(--ink);line-height:1}
  .top-contact{left:590px;top:6px;font-size:10px;color:#444;display:flex;gap:10px;align-items:center}
  .top-contact span{display:flex;align-items:center;gap:5px}
  .top-contact .sep{width:1px;height:12px;background:#ccc}
  .social{left:692px;top:31px;display:flex;gap:4px}
  .social i{display:block;width:15px;height:15px;border-radius:3px;background:var(--teal)}

  /* nav */
  .main-nav{left:68px;top:57px;width:683px;height:31px;border-radius:0 0 8px 8px;background:linear-gradient(#3bb7a3,var(--teal-dark))}
  .main-nav a{position:absolute;top:8px;font-size:12px;color:var(--white);text-decoration:none}
  .main-nav .current::after{content:"";position:absolute;left:50%;bottom:-8px;margin-left:-3px;border:3px solid transparent;border-bottom-color:var(--red)}
  .search{position:absolute;left:510px;top:5px;width:160px;height:21px;background:var(--white);border-radius:5px;font-size:10px;color:#999;padding:4px 11px}
  .search svg{position:absolute;right:6px;top:4px}

  /* hero */
  .hero{left:70px;top:100px;width:681px;height:367px;border-radius:5px;overflow:hidden;
    background:linear-gradient(180deg,#7fb3e6 0%,#9fc6ea 35%,#a05a44 50%,#7a4436 62%,#5b4b40 78%,#5d7f95 100%)}
  .hero-lead{left:362px;top:128px;width:394px;text-align:center;font-family:"Encode Sans Condensed",sans-serif;font-weight:300;font-size:18.5px;line-height:24px;color:var(--white)}
  .hero-banner{left:373px;top:185px;width:366px;height:32px;background:rgba(231,241,250,.93);text-align:center;font-family:"Fjalla One",sans-serif;font-size:16px;letter-spacing:2px;line-height:32px;color:#111}
  .hero-cta{left:479px;top:231px;width:169px;height:34px;background:var(--green);border:1px solid #7bd0a6;border-radius:3px;text-align:center;font-family:"Encode Sans Condensed",sans-serif;font-weight:300;font-size:19px;line-height:32px;color:var(--white)}

  /* featured services */
  .featured{left:0;top:481px;width:821px;height:279px;background:linear-gradient(#ececec,#f7f7f7 45%,#fff)}
  .section-title{font-family:"Fjalla One",sans-serif;font-weight:400;font-size:19px;letter-spacing:2px;color:#222}
  .featured .section-title{left:0;width:821px;top:24px;text-align:center}
  .featured-intro{left:75px;top:66px;width:671px;text-align:center;font-size:10.2px;line-height:16px;color:#555}
  .featured-rule{left:90px;top:116px;width:641px;height:1px;background:#ddd}
  .service{width:220px;height:80px}
  .service-icon{position:absolute;left:0;top:0;width:68px;height:68px;border-radius:50%;background:#bfe7df}
  .service-body{position:absolute;left:77px;top:-6px;height:76px;border-left:1px solid #ccc;padding-left:11px;width:135px}
  .service-body h3{font-family:"Fjalla One",sans-serif;font-weight:400;font-size:11.5px;letter-spacing:.3px;color:#111;margin-bottom:6px}
  .service-body p{font-size:8px;line-height:10px;color:#777;width:118px}

  /* let's talk */
  .talk{left:0;top:760px;width:821px;height:215px;background:linear-gradient(90deg,#d8e7ee,#e6eff3 55%,#dde8ed);border-top:1px solid #d4dde0}
  .talk-person{left:110px;top:735px;width:195px;height:240px;border-radius:90px 90px 0 0;background:linear-gradient(#8a6a52 0%,#c9a38a 30%,#f3f3f3 55%,#fff 100%)}
  .talk .section-title{left:345px;top:18px}
  .talk-copy{left:344px;top:56px;width:412px;font-size:10.4px;line-height:15.5px;color:#333}
  .talk-links{left:345px;top:138px;font-family:Arial,sans-serif;font-size:11.5px;color:var(--teal);display:flex;gap:14px}
  .talk-links .chat{color:var(--red)}

  /* footer */
  .site-footer{left:0;top:975px;width:821px;height:180px;background:linear-gradient(var(--footer-top),var(--footer-bottom));border-top:4px solid #3aa86f;color:var(--white)}
  .footer-col{top:28px}
  .footer-col h4{font-weight:400;font-size:15px;margin-bottom:12px}
  .footer-services{left:68px}
  .footer-services p{font-size:10px;line-height:11.5px;margin-left:2px}
  .more{display:inline-block;margin-top:6px;margin-left:3px;background:var(--red);font-size:8px;padding:1px 4px;border-radius:1px}
  .footer-news{left:200px;width:200px}
  .news-item{margin:6px 5px 14px;font-size:8px;line-height:10px}
  .news-item b{display:block;font-weight:400;margin-bottom:5px}
  .footer-letter{left:425px;width:150px}
  .footer-letter small{display:block;font-size:8px;margin-bottom:7px}
  .email-field{width:146px;height:21px;background:var(--white);color:#333;font-size:8px;padding:5px 9px}
  .submit{margin-top:11px;width:71px;height:19px;background:var(--red);font-size:8px;letter-spacing:2px;text-align:center;line-height:19px}
  .footer-contact{left:597px;width:190px;font-size:9px}
  .footer-contact address{font-style:normal;line-height:12px;margin-bottom:14px}
  .footer-contact p{display:flex;align-items:center;gap:7px;font-size:11px;margin-bottom:14px}

  .footer-bar{left:0;top:1155px;width:821px;height:45px;background:var(--dark);color:var(--white);font-size:8.5px}
  .footer-bar nav{position:absolute;left:68px;top:18px}
  .footer-bar nav span{margin:0 6px}
  .copyright{position:absolute;right:70px;top:18px}
</style>
</head>
<body>

<header class="site-header abs">
  <div class="brand abs"><i class="brand-mark"></i><span class="brand-name">KRMV</span></div>
  <div class="top-contact abs">
    <span><svg width="10" height="8" viewBox="0 0 10 8"><rect width="10" height="8" rx="1" fill="#2fae9c"/><path d="M0 1l5 3.5L10 1" stroke="#fff" fill="none"/></svg>info@krmv.com</span>
    <i class="sep"></i>
    <span><svg width="9" height="9" viewBox="0 0 10 10"><path d="M2 0l2 2.5-1.2 1.3a6 6 0 003.4 3.4L7.5 6 10 8 8.5 10C4 10 0 6 0 1.5z" fill="#2fae9c"/></svg>555 210 3846</span>
  </div>
  <div class="social abs"><i></i><i></i><i></i></div>
</header>

<nav class="main-nav abs">
  <a class="current" style="left:29px">Home</a>
  <a style="left:94px">About us</a>
  <a style="left:174px">Services ▾</a>
  <a style="left:250px">Contact us</a>
  <div class="search">Search site
    <svg width="12" height="12" viewBox="0 0 12 12"><circle cx="5" cy="5" r="3.8" stroke="#2fae9c" stroke-width="1.8" fill="none"/><path d="M8 8l3 3" stroke="#2fae9c" stroke-width="2"/></svg>
  </div>
</nav>

<section class="hero abs" role="img" aria-label="Photo of a row of red-brick townhouses beside a canal under a blue sky"></section>
<p class="hero-lead abs">We Provide Solution to Develope Residential Sites into<br>Multiple Townhouses, Units, and Apartments.</p>
<div class="hero-banner abs">UNLOCK THE VALUE OF YOUR PROPERTY</div>
<div class="hero-cta abs">Lets Get Started</div>

<section class="featured abs">
  <h2 class="section-title abs">Featured Services</h2>
  <p class="featured-intro abs">Lorem ipsum dolor sit amet, consectetur adipiscing elit. Nam venenatis ut lacus nec porta. Cras aliquet arcu a eros feugiat vestibulum.<br>Ut enim ipsum, blandit eu nulla non, cursus tincidunt magna.</p>
  <div class="featured-rule abs"></div>

  <div class="service abs" style="left:63px;top:157px">
    <div class="service-icon" role="img" aria-label="Illustration of a house with a price tag"></div>
    <div class="service-body"><h3>Financial</h3><p>Etiam euismod risus et ligula facilisis volutpat. Curabitur faucibus dapibus metus, placerat accumsan libero iaculis eget.</p></div>
  </div>
  <div class="service abs" style="left:297px;top:157px">
    <div class="service-icon" role="img" aria-label="Illustration of charts under a magnifying glass"></div>
    <div class="service-body"><h3>Consulting</h3><p>Etiam euismod risus et ligula facilisis volutpat. Curabitur faucibus dapibus metus, placerat accumsan libero iaculis eget.</p></div>
  </div>
  <div class="service abs" style="left:548px;top:163px">
    <div class="service-icon" role="img" aria-label="Illustration of a report on a computer screen"></div>
    <div class="service-body"><h3>Reports</h3><p>Etiam euismod risus et ligula facilisis volutpat. Curabitur faucibus dapibus metus, placerat accumsan libero iaculis eget.</p></div>
  </div>
</section>

<section class="talk abs" role="img" aria-label="Faded photo of apartment buildings">
  <h2 class="section-title abs">Let’s Talk</h2>
  <p class="talk-copy abs">Lorem ipsum dolor sit amet, consectetur adipiscing elit. Nulla ac bibendum est. Etiam eu sapien in augue maximus fringilla. Sed tincidunt, nunc ac luctus faucibus, lacus orci tincidunt nisl, at pretium purus nisi in leo. Etiam non dignissim tortor. Cum sociis natoque penatibus et magnis dis parturient montes, nascetur ridiculus mus.</p>
  <div class="talk-links abs"><span>info@krmv.com</span><span>|</span><span>555.210.3846</span><span>|</span><span class="chat">Live Chat</span></div>
</section>
<div class="talk-person abs" role="img" aria-label="Photo of a support agent wearing a headset"></div>

<footer class="site-footer abs">
  <div class="footer-col footer-services abs">
    <h4>Services</h4>
    <p>Lorem ipsum<br>Dolor sit amet,<br>Consectetur adipiscing<br>Elit Nulla ac<br>Bibendum est<br>Etiam eu sapien in<br>Augue maximus fringilla</p>
    <span class="more">more..</span>
  </div>
  <div class="footer-col footer-news abs">
    <h4>Recent News</h4>
    <div class="news-item"><b>01-04-2015</b>Lorem ipsum dolor sit amet, consectetur adipi-scing elit. Nulla ac bibendum est. Etiam eu sapien</div>
    <div class="news-item"><b>01-04-2015</b>Lorem ipsum dolor sit amet, consectetur adipi-scing elit. Nulla ac bibendum est. Etiam eu sapien</div>
  </div>
  <div class="footer-col footer-letter abs">
    <h4>Newsletter</h4>
    <small>Lorem ipsum dolor sit amet</small>
    <div class="email-field">Email Address</div>
    <div class="submit">SUBMIT</div>
  </div>
  <div class="footer-col footer-contact abs">
    <h4>Contact info</h4>
    <address>48 Sample Lane, Harbour House,<br>2nd floor, Sample State, USA.</address>
    <p><svg width="11" height="8" viewBox="0 0 10 8"><rect width="10" height="8" rx="1" fill="#2b3838"/><path d="M0 1l5 3.5L10 1" stroke="#fff" fill="none"/></svg>info@krmv.com</p>
    <p><svg width="10" height="10" viewBox="0 0 10 10"><path d="M2 0l2 2.5-1.2 1.3a6 6 0 003.4 3.4L7.5 6 10 8 8.5 10C4 10 0 6 0 1.5z" fill="#2b3838"/></svg>555 210 3846</p>
  </div>
</footer>

<div class="footer-bar abs">
  <nav>Home<span>|</span>About us<span>|</span>Contact us</nav>
  <div class="copyright">Copyright 2015 krmv.com All Rights Reserved.</div>
</div>

</body>
</html>
```